redesign of www.torvalo.com

Need redesign of our website to be more professionally looking. International import & export, warehousing and distribution business primarily from China to North America.

A few professional pictures needed on the new website.

Contact form also is needed.

Total 5 - 10 pages will be OK.

```html
<!DOCTYPE html>
<html lang="en">
<head>
<meta charset="utf-8">
<title>Torvalo – Your Partner in Global Trade</title>
<link rel="stylesheet" href="https://fonts.googleapis.com/css2?family=Yanone+Kaffeesatz:wght@400;700&family=Roboto:wght@300;400;500;700&family=PT+Sans:wght@400;700&display=swap">
<style>
:root{
  --orange:#f39c12;
  --orange-deep:#e07b0b;
  --ink:#2d3340;
  --navy:#3a4356;
  --grey-text:#6e737b;
  --muted:#8b9098;
  --panel:#eef0f1;
  --footer:#e4e6e8;
  --link:#3f5a86;
  --white:#ffffff;
}
*{margin:0;padding:0;box-sizing:border-box}
html,body{width:1024px;height:1200px;overflow:hidden}
body{position:relative;background:var(--panel);font-family:"Roboto",sans-serif;color:var(--grey-text)}

/* header */
.site-header{position:absolute;left:0;top:0;width:1024px;height:83px;background:var(--white);border-top:3px solid var(--ink)}
.phone-tab{position:absolute;left:602px;top:0;width:290px;height:26px;background:var(--ink);border-radius:0 0 14px 14px;color:#fff;font:700 12px "PT Sans",sans-serif;display:flex;align-items:center;justify-content:center;gap:7px}
.phone-tab b{color:var(--orange)}
.brand{position:absolute;left:126px;top:20px;display:flex;align-items:center;gap:10px}
.brand-dot{width:14px;height:14px;border-radius:50%;background:var(--orange)}
.brand-name{font:700 40px/1 "Yanone Kaffeesatz",sans-serif;color:var(--ink);letter-spacing:1px}
.nav{position:absolute;top:47px;left:494px;display:flex;gap:28px;font:700 15px "Yanone Kaffeesatz",sans-serif;letter-spacing:.5px;color:#7b8089}
.nav .active{color:var(--navy)}
.contact-btn{position:absolute;left:775px;top:35px;width:111px;height:36px;background:linear-gradient(#f7b033,var(--orange-deep));border-radius:3px;color:#fff;font:700 15px "Yanone Kaffeesatz",sans-serif;display:flex;align-items:center;justify-content:center;gap:8px}

/* hero */
.hero{position:absolute;left:0;top:83px;width:1024px;height:397px;background:linear-gradient(160deg,#6f7d52 0%,#8f9a7a 30%,#b9bec0 55%,#7d8a63 80%,#5f6d44 100%)}
.hero-title{position:absolute;left:134px;top:32px;font:700 35px "Yanone Kaffeesatz",sans-serif;color:#fff}
.hero-copy{position:absolute;left:138px;top:82px;width:480px;font:400 14px/17px "PT Sans",sans-serif;letter-spacing:-.2px;color:#fff}
.arrow{position:absolute;top:154px;width:36px;height:36px;border-radius:50%;display:flex;align-items:center;justify-content:center}
.arrow.prev{left:78px;background:var(--orange);border:3px solid #f6c06a}
.arrow.next{left:904px;background:#3a3f46;border:3px solid #5a6068}

/* content panel */
.panel{position:absolute;left:108px;top:438px;width:803px;height:560px;background:radial-gradient(ellipse at 60% 30%,#e3e6e8,#f2f3f4 70%);box-shadow:0 0 30px rgba(0,0,0,.08)}
.photo{position:absolute;background:linear-gradient(135deg,#b8cbe0,#5d7ba0 60%,#dfe7ef)}
.section-title{position:absolute;font:700 20px "Yanone Kaffeesatz",sans-serif;color:var(--ink)}
.body-copy{position:absolute;font:300 10px/16px "Roboto",sans-serif;color:var(--grey-text)}
.learn-btn{position:absolute;left:311px;top:659px;width:64px;height:27px;border:1px solid #cfd2d5;border-radius:3px;background:linear-gradient(#fafafa,#e9eaeb);font:400 9px "Roboto",sans-serif;color:var(--muted);display:flex;align-items:center;justify-content:center}

/* service cards */
.card{position:absolute;top:719px;width:237px;height:271px;background:#fff;border-top:6px solid var(--orange-deep);box-shadow:0 1px 4px rgba(0,0,0,.15)}
.card h3{position:absolute;top:22px;left:0;width:100%;text-align:center;font:700 18px "Yanone Kaffeesatz",sans-serif;color:var(--ink)}
.card .card-img{position:absolute;left:18px;top:48px;width:200px;height:105px}
.card p{position:absolute;left:20px;top:172px;width:205px;font:400 11px/15px "Roboto",sans-serif;color:var(--grey-text)}
.card .more{position:absolute;left:20px;top:232px;font:700 11px "Roboto",sans-serif;color:var(--link);text-decoration:underline}

/* footer */
.site-footer{position:absolute;left:0;top:1018px;width:1024px;height:147px;background:var(--footer);border-top:1px solid #d6d8da}
.f-brand{position:absolute;left:132px;top:54px;display:flex;align-items:center;gap:7px}
.f-brand .brand-name{font-size:28px}
.f-brand .brand-dot{width:10px;height:10px}
.f-col{position:absolute;top:31px}
.f-col h4{font:500 11.5px "Roboto",sans-serif;color:#6b7079;margin-bottom:11px}
.f-col li{list-style:none;font:400 8.8px/19px "Roboto",sans-serif;color:var(--muted)}
.f-col li::before{content:"";display:inline-block;border-left:3px solid #9aa0a6;border-top:3px solid transparent;border-bottom:3px solid transparent;margin-right:7px}
.f-col li.current{color:var(--orange)}
.contact-row{display:flex;align-items:flex-start;gap:10px;font:400 8.8px/19px "Roboto",sans-serif;color:var(--muted)}
.contact-row svg{margin-top:4px;flex:none}
.socials{display:flex;gap:9px}
.social{width:28px;height:28px;border-radius:2px;box-shadow:0 2px 3px rgba(0,0,0,.2)}
.bottom-bar{position:absolute;left:0;top:1165px;width:1024px;height:35px;background:var(--orange);font:400 8.8px "Roboto",sans-serif;color:#5a3a06}
.bottom-bar .copy{position:absolute;left:134px;top:12px}
.bottom-bar .legal{position:absolute;left:778px;top:12px}
</style>
</head>
<body>

<header class="site-header">
  <div class="phone-tab">
    <svg width="14" height="14" viewBox="0 0 16 16"><circle cx="8" cy="8" r="7" fill="none" stroke="#fff" stroke-width="1.3"/><path d="M5.5 4.5l1.3 1.6-.8 1c.5 1 1.2 1.7 2.1 2.2l1-.8 1.6 1.3-.8 1.3C7.3 11 5 8.7 4.3 5.3z" fill="#fff"/></svg>
    FOR INQUIRIES, CALL US: <b>1-800-555-01992</b>
  </div>
  <div class="brand">
    <span class="brand-dot"></span>
    <span class="brand-name">TORVALO</span>
  </div>
  <nav class="nav">
    <span class="active">HOME</span><span>ABOUT US</span><span>SERVICES</span><span>SERVICES</span>
  </nav>
  <div class="contact-btn">
    <svg width="18" height="13" viewBox="0 0 18 13"><rect x="1" y="1" width="16" height="11" rx="1" fill="none" stroke="#fff" stroke-width="1.5"/><path d="M1 1l8 6 8-6" fill="none" stroke="#fff" stroke-width="1.5"/></svg>
    CONTACT US
  </div>
</header>

<section class="hero" role="img" aria-label="Highway viaduct curving through green hills with a yellow truck">
  <h1 class="hero-title">Your Partner in Global Trade</h1>
  <p class="hero-copy">We are committed to utilize the MOST COST EFFECTIVE resources to help our clients in product development, prototyping, sampling, manufacturing, arranging custom clearance &amp; shipment delivery to the door in a hassle free environment.</p>
  <div class="arrow prev"><svg width="8" height="10"><path d="M6 1L2 5l4 4" fill="none" stroke="#fff" stroke-width="1.6"/></svg></div>
  <div class="arrow next"><svg width="8" height="10"><path d="M2 1l4 4-4 4" fill="none" stroke="#fff" stroke-width="1.6"/></svg></div>
</section>

<section class="panel" role="img" aria-label="Faint world map background with connecting routes"></section>

<div class="photo" style="left:136px;top:478px;width:158px;height:210px" role="img" aria-label="Business handshake"></div>
<h2 class="section-title" style="left:311px;top:470px">Welcome to Torvalo Inc.</h2>
<p class="body-copy" style="left:313px;top:504px;width:290px">It is a long established fact that a reader will be distracted by the readable content of a page when looking at its layout. The point of using Lorem Ipsum is that it has a more-or-less normal distribution of letters, as opposed to using 'Content here, content here', making it look like readable English.</p>
<p class="body-copy" style="left:313px;top:600px;width:290px">Lorem ipsum dolor sit amet, consectetur adipisicing elit, sed do eiusmod tempor incididunt ut labore et dolore magna aliqua. Ut enim ad minim veniam, quis nostrud exercitation ullamco laboris</p>
<div class="learn-btn">Learn More</div>

<h2 class="section-title" style="left:649px;top:470px">Torvalo Goal</h2>
<p class="body-copy" style="left:647px;top:504px;width:240px">It is a long established fact that a reader will be distracted by the readable content of a page when looking at its layout. The point of using Lorem Ipsum is that it has a more-or-less normal distribution</p>
<h2 class="section-title" style="left:649px;top:590px">Torvalo Principle</h2>
<p class="body-copy" style="left:647px;top:624px;width:240px">It is a long established fact that a reader will be distracted by the readable content of a page when looking at its layout. The point of using Lorem Ipsum is that it has a more-or-less normal distribution</p>

<article class="card" style="left:133px">
  <h3>IMPORT &amp; EXPORT</h3>
  <div class="card-img" style="background:linear-gradient(180deg,#c9d9e6,#8aa4bb 45%,#3a4a5c)" role="img" aria-label="Container ship at sea"></div>
  <p>Lorem ipsum dolor sit amet, consectetur adipisicing elit, sed do eiusmod tempor incididunt ut labore .</p>
  <span class="more">READ MORE</span>
</article>
<article class="card" style="left:390px">
  <h3>WAREHOUSING &amp; DISTRIBUTION</h3>
  <div class="card-img" style="background:linear-gradient(180deg,#8b6a44,#c89a5c 50%,#e6e3dc)" role="img" aria-label="Warehouse with shelves of boxes and a forklift"></div>
  <p>Lorem ipsum dolor sit amet, consectetur adipisicing elit, sed do eiusmod tempor incididunt ut labore .</p>
  <span class="more">READ MORE</span>
</article>
<article class="card" style="left:647px">
  <h3>SOURCING</h3>
  <div class="card-img" style="background:linear-gradient(135deg,#c89a7e,#eef1f3 50%,#6f8aa6)" role="img" aria-label="Team of colleagues reviewing documents"></div>
  <p>Lorem ipsum dolor sit amet, consectetur adipisicing elit, sed do eiusmod tempor incididunt ut labore .</p>
  <span class="more">READ MORE</span>
</article>

<footer class="site-footer">
  <div class="f-brand">
    <span class="brand-dot"></span>
    <span class="brand-name">TORVALO</span>
  </div>
  <div class="f-col" style="left:321px">
    <h4>Navigation</h4>
    <ul><li>Home</li><li>About</li><li>Services</li><li>Contact</li></ul>
  </div>
  <div class="f-col" style="left:448px">
    <h4>Services</h4>
    <ul><li class="current">Service</li><li>Service</li><li>Service</li><li>Service</li></ul>
  </div>
  <div class="f-col" style="left:577px">
    <h4>Contact Us</h4>
    <div class="contact-row"><svg width="9" height="11" viewBox="0 0 9 11"><path d="M1 1l2.5 0 .8 2.5-1.3 1c.6 1.3 1.4 2.2 2.6 2.8l1-1.2L9 7v2.5C4.5 9.5 1 5.5 1 1z" fill="#9aa0a6"/></svg>+1800-555-0199</div>
    <div class="contact-row" style="margin-top:5px"><svg width="10" height="8" viewBox="0 0 10 8"><rect width="10" height="8" fill="#9aa0a6"/><path d="M0 0l5 4 5-4" fill="none" stroke="#fff"/></svg>info@yourwebsite.com</div>
    <div class="contact-row" style="margin-top:5px"><svg width="9" height="12" viewBox="0 0 9 12"><path d="M4.5 0C2 0 0 2 0 4.3 0 7.5 4.5 12 4.5 12S9 7.5 9 4.3C9 2 7 0 4.5 0z" fill="#9aa0a6"/><circle cx="4.5" cy="4.3" r="1.6" fill="#e4e6e8"/></svg><span>Your Address, Your Country<br>Your Zip Code</span></div>
  </div>
  <div class="f-col" style="left:750px">
    <h4>Social</h4>
    <div class="socials">
      <span class="social" style="background:#3b5a95" role="img" aria-label="Social profile"></span>
      <span class="social" style="background:#2aa3db" role="img" aria-label="Social profile"></span>
      <span class="social" style="background:#1e6ca3" role="img" aria-label="Social profile"></span>
      <span class="social" style="background:#d5402f" role="img" aria-label="Social profile"></span>
    </div>
  </div>
</footer>
<div class="bottom-bar">
  <span class="copy">Copyright 2014 © Torvalo - All Rights Reserved</span>
  <span class="legal">Site Map &nbsp; • &nbsp; Privacy Policy</span>
</div>

</body>
</html>
```